VELTRIX GROUP
Project: VXG LOGO
VXG LOGO - Trade
VXG LOGO
Use same font as used in my logo
FAISAL NOORi
GENERAL MANAGER
RIYADH
info@veltrixgroup-example.com
VXGROUP VXGROUP
following changes on your design no #158 the logo upper and left side of the letter head company name bottom and left side of the letter haead The business cards are also in the above pattern. waiting for your immediate response. thanks.

```html
<!DOCTYPE html>
<html lang="en">
<head>
<meta charset="utf-8">
<title>Veltrix Group – Business Card</title>
<link rel="stylesheet" href="https://fonts.googleapis.com/css2?family=Roboto:wght@400;700;900&display=swap">
<style>
  :root {
    --backdrop: #f1f1f1;
    --brand-blue: #1b5ba7;
    --white: #ffffff;
  }
  html, body {
    margin: 0;
    padding: 0;
    width: 1200px;
    height: 871px;
    overflow: hidden;
    background: var(--backdrop);
    font-family: "Roboto", Arial, sans-serif;
  }
  .card {
    position: absolute;
    left: 151px;
    top: 185px;
    width: 898px;
    height: 494px;
    background: var(--brand-blue);
  }
  .divider {
    position: absolute;
    left: 449px;
    top: 55px;
    width: 2px;
    height: 384px;
    background: rgba(255,255,255,0.8);
  }
  .name-banner {
    position: absolute;
    left: 0;
    top: 96px;
    width: 360px;
    height: 44px;
  }
  .person-name {
    position: absolute;
    left: 53px;
    top: 99px;
    margin: 0;
    font-size: 30px;
    font-weight: 700;
    color: var(--brand-blue);
    letter-spacing: 0.5px;
  }
  .person-role {
    position: absolute;
    left: 53px;
    top: 142px;
    margin: 0;
    font-size: 15px;
    font-weight: 700;
    color: var(--white);
    letter-spacing: 0.3px;
  }
  .contact-list {
    position: absolute;
    left: 40px;
    top: 218px;
    margin: 0;
    padding: 0;
    list-style: none;
  }
  .contact-item {
    display: flex;
    align-items: center;
    height: 40px;
    color: var(--white);
    font-size: 24px;
  }
  .contact-icon {
    width: 26px;
    height: 26px;
    margin-right: 16px;
    flex: none;
  }
  .brand-mark {
    position: absolute;
    left: 545px;
    top: 150px;
    margin: 0;
    font-size: 132px;
    font-weight: 900;
    line-height: 1;
    color: var(--white);
    letter-spacing: -4px;
  }
  .brand-name {
    position: absolute;
    left: 549px;
    top: 312px;
    margin: 0;
    font-size: 31px;
    font-weight: 700;
    color: var(--white);
  }
</style>
</head>
<body>
  <section class="card">
    <svg class="name-banner" viewBox="0 0 360 44" aria-hidden="true">
      <polygon points="0,0 360,0 340,44 0,44" fill="#ffffff"/>
    </svg>
    <h1 class="person-name">FAISAL NOORi</h1>
    <p class="person-role">GENERAL MANAGER</p>

    <ul class="contact-list">
      <li class="contact-item">
        <svg class="contact-icon" viewBox="0 0 26 26" aria-hidden="true">
          <circle cx="13" cy="13" r="12" fill="#fff"/>
          <rect x="6.5" y="8.5" width="13" height="9" fill="none" stroke="#1b5ba7" stroke-width="1.6"/>
          <polyline points="6.5,8.5 13,13.5 19.5,8.5" fill="none" stroke="#1b5ba7" stroke-width="1.6"/>
        </svg>
        info@veltrixgroup-example.com
      </li>
      <li class="contact-item">
        <svg class="contact-icon" viewBox="0 0 26 26" aria-hidden="true">
          <circle cx="13" cy="13" r="12" fill="#fff"/>
          <circle cx="13" cy="13" r="6.5" fill="none" stroke="#1b5ba7" stroke-width="1.5"/>
          <ellipse cx="13" cy="13" rx="3" ry="6.5" fill="none" stroke="#1b5ba7" stroke-width="1.3"/>
          <line x1="6.5" y1="13" x2="19.5" y2="13" stroke="#1b5ba7" stroke-width="1.3"/>
        </svg>
        www@vxg-example.com
      </li>
      <li class="contact-item">
        <svg class="contact-icon" viewBox="0 0 26 26" aria-hidden="true">
          <circle cx="13" cy="13" r="12" fill="#fff"/>
          <path d="M13 20 C9 15 8.5 13 8.5 11 a4.5 4.5 0 0 1 9 0 c0 2 -0.5 4 -4.5 9z" fill="#1b5ba7"/>
          <circle cx="13" cy="11" r="1.7" fill="#fff"/>
        </svg>
        Riyadh, Saudi Arabia
      </li>
      <li class="contact-item">
        <svg class="contact-icon" viewBox="0 0 26 26" aria-hidden="true">
          <circle cx="13" cy="13" r="12" fill="#fff"/>
          <path d="M9 7 l3 3 -1.5 2 c1 2 2 3 3.5 3.5 l2 -1.5 3 3 -2 2 c-5 0 -10 -5 -10 -10z" fill="#1b5ba7"/>
        </svg>
        +96610000111
      </li>
      <li class="contact-item">
        <svg class="contact-icon" viewBox="0 0 26 26" aria-hidden="true">
          <circle cx="13" cy="13" r="12" fill="#fff"/>
          <rect x="7" y="11" width="12" height="8" fill="#1b5ba7"/>
          <rect x="9.5" y="7" width="7" height="4" fill="none" stroke="#1b5ba7" stroke-width="1.4"/>
        </svg>
        +96610000222
      </li>
    </ul>

    <div class="divider"></div>

    <p class="brand-mark">VXG</p>
    <p class="brand-name">VELTRIX GROUP</p>
  </section>
</body>
</html>
```